Looking for something sharp classy and with an edge for an advanced civil construction business
Something that says professional
nothing too DARK

Target Market(s)

mining companies council civil contractors concrete works

Industry/Entity Type

Construction

Contact Information for Business Card

Brindle Civil Constructions
brindlecivilconstruction@quokkamail.com
Tavi Marlowe
0418275936

Font styles to use
Serif
Sans Serif

Colors
0455a3
0592cd
85cae6
000000
919191

Requirements
Must have
• On the back of the card must have
down the bottom small print email logo phone number

Should not have
• follow us on facebook
Brindle Civil Constructions

follow us on instagram
BRINDLECIVILCONSTRUCTIONS

```html
<!DOCTYPE html>
<html lang="en">
<head>
<meta charset="utf-8">
<title>Brindle Civil Constructions – Business Card</title>
<link href="https://fonts.googleapis.com/css2?family=PT+Serif:wght@400;700&display=swap" rel="stylesheet">
<style>
  :root {
    --stage: #e9e7e4;
    --card-front: #1eaee6;
    --card-back: #0b0c26;
    --ink: #000000;
    --ink-light: #ffffff;
    --shadow: rgba(0, 0, 0, 0.18);
  }
  * { box-sizing: border-box; margin: 0; padding: 0; }
  html, body { width: 1200px; height: 960px; overflow: hidden; }
  body {
    background: var(--stage);
    font-family: "PT Serif", Georgia, serif;
    display: flex;
    align-items: center;
    justify-content: center;
    gap: 60px;
  }
  .card {
    position: relative;
    width: 520px;
    height: 300px;
    box-shadow: 0 10px 26px var(--shadow);
  }
  /* Back side */
  .card--back { background: var(--card-back); color: var(--ink-light); }
  .back-footer {
    position: absolute;
    left: 34px;
    bottom: 28px;
  }
  .back-brand {
    font-weight: 700;
    font-size: 20px;
    line-height: 1;
    margin-bottom: 12px;
  }
  .back-contact { list-style: none; font-size: 11.5px; line-height: 1.6; }
  .back-contact li { display: flex; align-items: center; gap: 7px; }
  .back-contact svg { width: 10px; height: 10px; fill: var(--ink-light); }
  /* Front side */
  .card--front {
    background: var(--card-front);
    color: var(--ink);
    display: flex;
    flex-direction: column;
    align-items: center;
    text-align: center;
    padding-top: 36px;
  }
  .front-brand { font-weight: 700; line-height: 1; }
  .front-brand__main { display: block; font-size: 58px; letter-spacing: 2px; text-transform: uppercase; }
  .front-brand__sub { display: block; font-size: 24px; margin-top: 4px; }
  .person { margin-top: 14px; }
  .person__name { font-weight: 700; font-size: 19px; letter-spacing: 0.5px; text-transform: uppercase; }
  .person__role { font-weight: 700; font-size: 16px; margin-top: 2px; }
  .front-contact { margin-top: 34px; font-size: 16px; line-height: 1.35; }
</style>
</head>
<body>
  <section class="card card--back" aria-label="Card back">
    <div class="back-footer">
      <div class="back-brand">Brindle</div>
      <ul class="back-contact">
        <li>
          <svg viewBox="0 0 10 10" aria-hidden="true"><path d="M2 0h2l1 3-1.5 1a6 6 0 0 0 2.5 2.5L7 5l3 1v2a2 2 0 0 1-2 2A8 8 0 0 1 0 2a2 2 0 0 1 2-2z"/></svg>
          0418275936
        </li>
        <li>
          <svg viewBox="0 0 10 10" aria-hidden="true"><path d="M0 2h10v6H0z M0 2l5 3.5L10 2" fill="none" stroke="#fff" stroke-width="1"/></svg>
          brindlecivilconstruction@quokkamail.com
        </li>
      </ul>
    </div>
  </section>

  <section class="card card--front" aria-label="Card front">
    <h1 class="front-brand">
      <span class="front-brand__main">Brindle</span>
      <span class="front-brand__sub">Civil Constructions</span>
    </h1>
    <div class="person">
      <p class="person__name">Tavi Marlowe</p>
      <p class="person__role">Director</p>
    </div>
    <div class="front-contact">
      <p>0418275936</p>
      <p>brindlecivilconstruction@quokkamail.com</p>
    </div>
  </section>
</body>
</html>
```